Geschäftspapier für Pfandhaus und Juwelier gesucht
Zielgruppe
Pfandhaus und Juwelier.
Aufgabenstellung
Ich betreibe mehrere Filialen und möchte all diese wir einem Briefkopf haben und ggf Platz für weitere da ich gerade 2 weitere eröffne. Unter www.leihhaus-Borlen.de sieht man Logo und Farben.
Ich möchte das Briefpapier als Datei haben und nicht gedruckt sondern will es selbst am Firmendrucker drucken.Die Bankverbindung sollte auch darauf sein aber erstmal etwas am Platzhalter eintragen .

```html
<!DOCTYPE html>
<html lang="de">
<head>
<meta charset="utf-8">
<title>Briefpapier Matthias Borlen Pfandkredit</title>
<link href="https://fonts.googleapis.com/css2?family=Open+Sans:wght@400;600;700&display=swap" rel="stylesheet">
<style>
  :root {
    --gold: #b09a62;
    --charcoal: #4a4a4a;
    --paper: #ffffff;
    --backdrop: #e9e9e9;
    --ink: #1c1c1c;
  }
  * { box-sizing: border-box; margin: 0; padding: 0; }
  html, body { width: 1200px; height: 1010px; overflow: hidden; }
  body {
    background: var(--backdrop);
    font-family: "Open Sans", Arial, sans-serif;
    color: var(--ink);
  }
  .sheet {
    position: absolute;
    left: 260px; top: 24px;
    width: 680px; height: 962px;
    background: var(--paper);
    box-shadow: 0 4px 18px rgba(0,0,0,.12);
    overflow: hidden;
  }
  .top-rule {
    position: absolute; left: 0; top: 0;
    width: 100%; height: 5px;
    background: var(--gold);
  }
  .brand-block {
    position: absolute; left: 66px; top: 0;
    width: 270px; height: 132px;
    background: var(--charcoal);
    display: flex; align-items: center; justify-content: center;
  }
  .brand-frame {
    width: 232px; height: 94px;
    border: 1px solid var(--gold);
    display: flex; align-items: center; justify-content: center;
  }
  .brand-name {
    color: var(--gold);
    font-weight: 400;
    font-size: 19px;
    letter-spacing: .5px;
    text-align: center;
    line-height: 1.35;
  }
  .branches {
    position: absolute; right: 0; top: 0;
    width: 214px;
    background: var(--gold);
    color: var(--paper);
    padding: 14px 14px 12px 18px;
    font-size: 7.6px;
    line-height: 1.34;
  }
  .branches-title { font-weight: 700; font-size: 8.4px; margin-bottom: 5px; }
  .branch { margin-bottom: 7px; }
  .branch:last-child { margin-bottom: 0; }
  .contact-line { display: flex; align-items: center; gap: 5px; padding-left: 10px; }
  .contact-line svg { width: 7px; height: 7px; flex: none; fill: var(--paper); }
  .sender-line {
    position: absolute; left: 66px; top: 172px;
    font-size: 6.8px;
    text-decoration: underline;
  }
  .recipient {
    position: absolute; left: 76px; top: 192px;
    font-size: 10.5px;
    line-height: 1.3;
    font-style: normal;
  }
  .fold-mark {
    position: absolute; left: 0;
    width: 16px; height: 1px;
    background: #bdbdbd;
  }
  .fold-mark.upper { top: 340px; }
  .fold-mark.lower { top: 644px; }
  .footer { position: absolute; left: 0; bottom: 0; width: 680px; height: 92px; }
  .footer svg { position: absolute; inset: 0; }
  .bank-details {
    position: absolute; left: 0; bottom: 12px;
    height: 38px; width: 500px;
    display: flex; align-items: center;
    color: var(--paper);
    font-size: 8.2px; line-height: 1.3;
    padding-left: 26px;
  }
  .bank-col { padding: 0 14px; border-left: 1px solid rgba(255,255,255,.8); }
  .bank-col:first-child { border-left: none; padding-left: 0; }
  .web-address {
    position: absolute; left: 512px; bottom: 12px;
    width: 142px; height: 58px;
    display: flex; align-items: center; justify-content: center;
    color: var(--paper); font-size: 9.5px;
    white-space: nowrap;
  }
</style>
</head>
<body>
  <main class="sheet">
    <div class="top-rule"></div>

    <div class="brand-block">
      <div class="brand-frame">
        <p class="brand-name">Matthias Borlen<br>Pfandkredit</p>
      </div>
    </div>

    <section class="branches">
      <p class="branches-title">MATTHIAS BORLEN PFANDKREDIT</p>
      <div class="branch">
        <p>Lindenhof 1</p><p>66100 Talbrück</p>
        <p class="contact-line"><svg viewBox="0 0 10 10"><path d="M2 0h2l1 3-1.5 1a6 6 0 0 0 2.5 2.5L7 5l3 1v2a2 2 0 0 1-2 2A8 8 0 0 1 0 2a2 2 0 0 1 2-2z"/></svg>+49 (0) 600 1110000-0</p>
        <p class="contact-line"><svg viewBox="0 0 10 10"><rect x="0" y="3" width="10" height="6"/><rect x="2" y="0" width="6" height="3"/></svg>+49 (0) 600 1110000-9</p>
        <p class="contact-line"><svg viewBox="0 0 10 10"><path d="M0 2h10v6H0z"/></svg>tb@leihhaus-borlen.de</p>
      </div>
      <div class="branch">
        <p>Am Weinberg 1</p><p>54200 Moselstadt</p>
        <p class="contact-line"><svg viewBox="0 0 10 10"><path d="M2 0h2l1 3-1.5 1a6 6 0 0 0 2.5 2.5L7 5l3 1v2a2 2 0 0 1-2 2A8 8 0 0 1 0 2a2 2 0 0 1 2-2z"/></svg>+49 (0) 600 2220000-5</p>
        <p class="contact-line"><svg viewBox="0 0 10 10"><rect x="0" y="3" width="10" height="6"/><rect x="2" y="0" width="6" height="3"/></svg>+49 (0) 600 2220000-0</p>
        <p class="contact-line"><svg viewBox="0 0 10 10"><path d="M0 2h10v6H0z"/></svg>ms@leihhaus-borlen.de</p>
      </div>
      <div class="branch">
        <p>Gleisweg 13</p><p>55100 Rheinau</p>
        <p class="contact-line"><svg viewBox="0 0 10 10"><path d="M2 0h2l1 3-1.5 1a6 6 0 0 0 2.5 2.5L7 5l3 1v2a2 2 0 0 1-2 2A8 8 0 0 1 0 2a2 2 0 0 1 2-2z"/></svg>+49 (0) 600 3330080</p>
        <p class="contact-line"><svg viewBox="0 0 10 10"><rect x="0" y="3" width="10" height="6"/><rect x="2" y="0" width="6" height="3"/></svg>+49 (0) 600 3330088</p>
        <p class="contact-line"><svg viewBox="0 0 10 10"><path d="M0 2h10v6H0z"/></svg>ra@leihhaus-borlen.de</p>
      </div>
      <div class="branch">
        <p>Uferstraße 108</p><p>65100 Quellbad</p>
        <p class="contact-line"><svg viewBox="0 0 10 10"><path d="M2 0h2l1 3-1.5 1a6 6 0 0 0 2.5 2.5L7 5l3 1v2a2 2 0 0 1-2 2A8 8 0 0 1 0 2a2 2 0 0 1 2-2z"/></svg>+49 (0) 600 44400767</p>
        <p class="contact-line"><svg viewBox="0 0 10 10"><rect x="0" y="3" width="10" height="6"/><rect x="2" y="0" width="6" height="3"/></svg>+49 (0) 600 44400912</p>
        <p class="contact-line"><svg viewBox="0 0 10 10"><path d="M0 2h10v6H0z"/></svg>qb@leihhaus-borlen.de</p>
      </div>
      <div class="branch">
        <p>Parkstr. 8</p><p>67600 Waldhain</p>
        <p class="contact-line"><svg viewBox="0 0 10 10"><path d="M2 0h2l1 3-1.5 1a6 6 0 0 0 2.5 2.5L7 5l3 1v2a2 2 0 0 1-2 2A8 8 0 0 1 0 2a2 2 0 0 1 2-2z"/></svg>+49 (0) 600 55440</p>
        <p class="contact-line"><svg viewBox="0 0 10 10"><path d="M0 2h10v6H0z"/></svg>wh@leihhaus-borlen.de</p>
      </div>
    </section>

    <p class="sender-line">Matthias Borlen Pfandkredit | Lindenhof 1 | 66100 Talbrück</p>
    <address class="recipient">
      Herr<br>Jonas Beispiel<br>Probeweg 13<br>24100 Nordfeld
    </address>

    <span class="fold-mark upper"></span>
    <span class="fold-mark lower"></span>

    <footer class="footer">
      <svg viewBox="0 0 680 92" width="680" height="92" aria-hidden="true">
        <polygon points="0,42 500,42 490,80 0,80" fill="var(--gold)"/>
        <polygon points="512,22 668,22 652,80 498,80" fill="var(--charcoal)"/>
        <polygon points="676,0 680,0 680,80 658,80" fill="var(--gold)"/>
      </svg>
      <div class="bank-details">
        <p class="bank-col">Bankverbindung:<br>Matthias Borlen</p>
        <p class="bank-col">Hausbank Mitte<br>USt-ID-Nr. DEXXXXXXXX</p>
        <p class="bank-col">IBAN: DEXX XXXX XXXX XXXX XXXX X<br>BIC: XXXXXXXX</p>
      </div>
      <p class="web-address">www.leihhaus-Borlen.de</p>
    </footer>
  </main>
</body>
</html>
```